DELMORAN Auto Battery

We need top of the line design for a new product that we are launching, Automotive Batteries.
We are an exporter of Auto Spare parts based in China, our new products will be launched in October 2012, the website is to be presented as B2B not B2C, we deal directly with Importers all around the world.
Our vision for the website is to be Clean, elegant, smart, warm, reflects confidence and trust..therefore, the choice of themes, colors, fonts and graphics should take into considerations all above.
Since there are hundreds of Battery types, specs, sizes, weight...etc, we will need a upload template that will enable us to upload, modify and manipulate the data of the batteries.
Car battery importers
Automotive

```html
<!DOCTYPE html>
<html lang="en">
<head>
<meta charset="utf-8">
<title>DELMORAN Auto Battery</title>
<link href="https://fonts.googleapis.com/css2?family=Source+Sans+3:wght@400;600;700&display=swap" rel="stylesheet">
<style>
:root{
  --space-deep:#05070f;
  --space-mid:#1a1738;
  --space-violet:#3b2552;
  --horizon:#5d7590;
  --cloud:#e6e9ee;
  --page:#d9d9db;
  --text-light:#f2f4f8;
  --text-body:#444a52;
  --heading:#3c434c;
  --nav-bg:#0b0c0e;
  --nav-edge:#3a3d42;
  --nav-active:#2a8fe0;
  --dot-active:#2d7fc4;
  --dot:#cfd3d8;
}
*{margin:0;padding:0;box-sizing:border-box}
html,body{width:1200px;height:1200px;overflow:hidden}
body{
  position:relative;
  font-family:"Source Sans 3",sans-serif;
  background:linear-gradient(180deg,var(--space-deep) 0px,var(--space-mid) 180px,var(--space-violet) 300px,var(--horizon) 500px,var(--cloud) 640px,#e2e3e6 760px,var(--page) 1200px);
}
.hero-sky{
  position:absolute;left:0;top:0;width:1200px;height:660px;
  background:
    radial-gradient(ellipse 420px 200px at 560px 250px,rgba(150,110,190,.35),transparent 70%),
    radial-gradient(ellipse 700px 160px at 600px 560px,rgba(255,255,255,.55),transparent 70%);
}
.brand{position:absolute;left:149px;top:58px;color:var(--text-light)}
.brand-name{font-size:44px;font-weight:600;letter-spacing:1px;line-height:1}
.brand-tag{font-size:27px;margin:6px 0 0 26px;line-height:1}
.search{
  position:absolute;left:891px;top:91px;width:189px;height:31px;
  background:linear-gradient(#fff,#e4e4e4);border:1px solid #999;
  font-size:16px;color:#444;padding:5px 0 0 8px;
}
.search svg{position:absolute;right:6px;top:6px}
.main-nav{
  position:absolute;left:69px;top:171px;width:1057px;height:59px;
  background:linear-gradient(#2b2d31,var(--nav-bg) 45%,#000);
  border:2px solid var(--nav-edge);border-radius:6px;
  box-shadow:0 4px 10px rgba(0,0,0,.6);
}
.main-nav ul{list-style:none;display:flex;gap:50px;position:absolute;left:94px;top:16px}
.main-nav li{color:#fff;font-size:20px}
.main-nav li.current,.footer-nav li.current{color:var(--nav-active)}
.slider-controls{
  position:absolute;left:983px;top:183px;width:104px;height:35px;
  background:#111;border:1px solid #444;border-radius:5px;
}
.slider-label{
  position:absolute;left:956px;top:229px;width:157px;height:31px;
  background:#0e0f11;border:1px solid #333;border-top:none;border-radius:0 0 5px 5px;
  color:#bbb;font-size:16px;text-align:center;padding-top:3px;
}
.hero-copy{position:absolute;left:128px;top:385px;width:428px;color:var(--text-light)}
.hero-copy h2{font-size:24px;font-weight:700;text-shadow:0 2px 3px rgba(0,0,0,.7);margin-bottom:6px}
.hero-copy p{font-size:20px;line-height:26.7px;text-align:justify}
.product-shot{
  position:absolute;left:696px;top:313px;width:357px;height:287px;border-radius:10px;
  background:linear-gradient(160deg,#2b2d31 0%,#6d7178 45%,#9ea2a8 100%);
}
.welcome{position:absolute;left:131px;top:692px;width:952px}
.welcome h1{text-align:center;font-size:36px;font-weight:400;color:var(--heading)}
.welcome hr{border:none;height:1px;margin:12px auto 16px;width:720px;background:linear-gradient(90deg,transparent,#aaa,transparent)}
.welcome p{font-size:20.5px;line-height:29.3px;color:var(--text-body);text-align:justify;text-align-last:left}
.site-footer{
  position:absolute;left:59px;top:1063px;width:1091px;height:80px;
  background:linear-gradient(#2a2c30,#0a0b0d 40%,#000);
  border:2px solid #333;border-radius:4px;
  box-shadow:0 18px 22px -8px rgba(0,0,0,.55);
}
.copyright{position:absolute;left:35px;top:30px;color:#fff;font-size:12px}
.footer-nav{list-style:none;display:flex;gap:37px;position:absolute;right:40px;top:27px}
.footer-nav li{color:#fff;font-size:16px}
</style>
</head>
<body>
<div class="hero-sky" role="img" aria-label="Starry night sky fading into bright clouds"></div>

<header class="brand">
  <div class="brand-name">DELMORAN</div>
  <div class="brand-tag">Auto Battery</div>
</header>

<div class="search">search here
  <svg width="18" height="18" viewBox="0 0 18 18"><circle cx="7" cy="7" r="5" fill="none" stroke="#444" stroke-width="2"/><line x1="11" y1="11" x2="16" y2="16" stroke="#444" stroke-width="2.5"/></svg>
</div>

<nav class="main-nav">
  <ul>
    <li class="current">Home</li><li>About Us</li><li>Products</li><li>Services</li><li>Our Clients</li><li>Contact Us</li>
  </ul>
</nav>

<div class="slider-controls">
  <svg width="104" height="35" viewBox="0 0 104 35">
    <circle cx="29" cy="16" r="8" fill="var(--dot-active)" stroke="#ddd" stroke-width="1.5"/>
    <circle cx="53" cy="16" r="8" fill="var(--dot)"/>
    <circle cx="76" cy="16" r="8" fill="var(--dot)"/>
  </svg>
</div>
<div class="slider-label">slider controls</div>

<section class="hero-copy">
  <h2>Put some text here</h2>
  <p>Since there are hundreds of Battery types, specs, sizes, weight...etc, we will need a upload template that will enable us to upload, modify and manipulate the data of the batteries.</p>
</section>

<div class="product-shot" role="img" aria-label="Product photo of a car battery"></div>

<main class="welcome">
  <h1>Welcome to our site</h1>
  <hr>
  <p>We need top of the line design for a new product that we are launching, Automotive Batteries.</p>
  <p>We are an exporter of Auto Spare parts based in China, our new products will be launched in October 2012, the website is to be presented as B2B not B2C, we deal directly with Importers all around the world.</p>
  <p>Our vision for the website is to be Clean, elegant, smart, warm, reflects confidence and trust..therefore, the choice of themes, colors, fonts and graphics should take into considerations all above. We need top of the line design for a new product that we are launching, Automotive Batteries.</p>
  <p>We are an exporter of Auto Spare parts based in China, our new products will be launched in October 2012, the website is to be presented as B2B not B2C, we deal directly with Importers all around the world.</p>
</main>

<footer class="site-footer">
  <div class="copyright">copyright © 2010 &nbsp;DELMORAN</div>
  <ul class="footer-nav">
    <li class="current">Home</li><li>About Us</li><li>Products</li><li>Services</li><li>Our Clients</li><li>Contact Us</li>
  </ul>
</footer>
</body>
</html>
```